Tidewell Claimworks Website - a medical billing website - one page

I need a one-page website to attract potential clients to my medical billing services - I am in the process of creating a logo, the contest ends Friday. I also have some ideas and am writing some of the copy that I can send you.

SLOGAN: We Turn Codes Into Money

MISSION STATEMENT: Give compassionate quality service and precision medical billing with urgency

Target Market(s)

MD's, physical therapists, occupational therapists, speech therapists, chiropractors, psychologists, psychiatrists, dentists and new grads of the above

Coding

Coded - Design and coding required

Number of Pages Required

1 page

Font styles to use
Sans Serif
Decorative
Script

Colors
33a6d7
add136
87cfc6
cadf82
9bcb3c
85cae6

Requirements
Must have
• I am working on the major points of copy that I need, plus
• ranking search terms keywords and phrases
Nice to have
• creativity to draw clients in
• my color choices below are similar to the logo coloring - but if you like something different feel free to use your own creative colors.

```html
<!DOCTYPE html>
<html lang="en">
<head>
<meta charset="utf-8">
<title>Tidewell Claimworks – Medical Billing</title>
<link href="https://fonts.googleapis.com/css2?family=Poppins:wght@300;400;500;600;700&display=swap" rel="stylesheet">
<style>
:root{
  --blue:#33a6d7;
  --green:#9bcb3c;
  --lime:#add136;
  --teal:#87cfc6;
  --sky:#85cae6;
  --ink:#1b1b1b;
  --deep:#1f3d4a;
  --grey:#f4f5f5;
  --text:#333;
  --muted:#666;
}
*{margin:0;padding:0;box-sizing:border-box}
html,body{width:1200px;height:4155px;overflow:hidden}
body{position:relative;font-family:"Poppins",sans-serif;color:var(--text);background:#fff}
.abs{position:absolute}
svg.abs{display:block}

/* header */
.site-header{left:0;top:0;width:1200px;height:116px;background:#0d0d0d}
.logo{font-weight:600;font-size:26px;color:var(--blue);letter-spacing:.2px;white-space:nowrap;line-height:1}
.site-header .logo{left:142px;top:44px}
.nav a{position:absolute;top:51px;font-size:12px;font-weight:500;color:#fff;text-decoration:none;letter-spacing:.3px}
.nav a.active{color:var(--lime)}

/* hero */
.hero-media{left:0;top:116px;width:1200px;height:690px;background:linear-gradient(90deg,#f3f4f4 0%,#eef0f1 35%,#dfe6ea 60%,#cdd8de 100%)}
.hero-title{left:144px;top:282px;font-size:64px;font-weight:700;color:var(--blue);line-height:1}
.hero-line{left:144px;font-size:18.5px;font-weight:600;color:var(--ink);text-transform:uppercase;white-space:nowrap}
.hero-line.accent{color:var(--green)}
.btn{display:flex;align-items:center;justify-content:center;gap:10px;background:#0d0d0d;color:var(--lime);font-size:14px;font-weight:500;text-decoration:none}
.btn svg{width:24px;height:10px}

/* about */
.about-frame{left:529px;top:895px;width:518px;height:491px;border:2px solid var(--green)}
.about-photo{left:0;top:965px;width:556px;height:421px;background:linear-gradient(90deg,#5cc9c2 0%,#3d7fc0 30%,#e8eef2 55%,#8fc6e6 80%,#ffffff 100%)}
.section-title{font-size:38px;font-weight:600;color:var(--blue);line-height:1.1}
.about-text{left:584px;top:1025px;width:422px;font-size:12.4px;line-height:18px;text-align:justify;color:var(--text)}

/* benefits */
.benefit-icon{width:106px;height:106px;border-radius:50%;background:linear-gradient(135deg,var(--green),#3fb3a1);box-shadow:0 8px 20px rgba(0,0,0,.12);display:flex;align-items:center;justify-content:center}
.benefit-label{width:220px;text-align:center;font-size:17px;line-height:26px;font-weight:300;color:var(--ink)}
.benefit-label b{font-weight:600}

/* services */
.service-photo{width:239px;height:239px;border-radius:50%;border:6px solid #e8e8e8;box-shadow:0 6px 18px rgba(0,0,0,.12)}
.service-photo.featured{border-color:var(--green)}
.service-name{width:260px;text-align:center;font-size:17px;font-weight:500;color:var(--blue);white-space:nowrap}
.service-desc{width:250px;text-align:center;font-size:11px;line-height:16px;color:var(--muted)}
.more{width:260px;display:flex;justify-content:center;align-items:center;gap:8px;font-size:13px;font-weight:500;color:var(--ink)}
.more svg{width:22px;height:10px}

/* tasks */
.tasks-band{left:0;top:2760px;width:1200px;height:473px;background:linear-gradient(100deg,#2fb4c8 0%,#4cc0c0 35%,#8fd3b0 58%,#d9ecd6 72%,#f1ebe4 100%)}
.tasks-title{left:142px;top:2852px;font-size:31px;font-weight:700;color:var(--deep);line-height:40px}
.task{left:142px;display:flex;align-items:center;gap:14px;font-size:21px;color:#fff}
.task svg{width:32px;height:32px}

/* testimonial */
.quote-photo{left:144px;top:3379px;width:243px;height:208px;border-radius:18px;background:#cfe6f1}
.quote-photo-inner{left:168px;top:3379px;width:196px;height:208px;background:linear-gradient(180deg,#e9edf0,#9fb3c5 60%,#51637b)}
.quote-text{left:406px;top:3398px;width:636px;font-size:12.4px;line-height:19.5px;color:var(--text);text-align:justify}
.client-name{left:406px;top:3506px;font-size:20px;color:var(--green)}
.client-role{left:406px;top:3535px;font-size:13px;color:var(--ink)}
.dot{width:11px;height:11px;border-radius:50%;background:#cfe8d8}
.dot.on{background:var(--green)}
.pager{width:56px;height:28px;border-radius:14px;border:1.5px solid var(--green);display:flex;align-items:center;justify-content:center}
.pager svg{width:24px;height:10px}

/* footer */
.footer-logo{left:142px;top:3872px}
.footer-text{left:142px;top:3934px;width:320px;font-size:12px;line-height:18.5px;color:#ddd}
.footer-head{font-size:23px;font-weight:600;color:#fff}
.quick-links{left:580px;top:3922px;list-style:none}
.quick-links li{font-size:12px;color:#ddd;height:28.6px;display:flex;align-items:center;gap:12px}
.quick-links li::before{content:"";width:4px;height:4px;border-radius:50%;background:#ddd}
.quick-links li.active{color:var(--lime)}
.contact-row{left:868px;display:flex;align-items:center;gap:14px;font-size:12.5px;color:#fff}
.contact-row svg{width:28px;height:22px}
.copyright{left:0;top:4122px;width:1200px;text-align:center;font-size:11px;color:#888}
</style>
</head>
<body>

<header class="site-header abs">
  <div class="logo abs">Tidewell Claimworks</div>
  <nav class="nav">
    <a href="#" class="active" style="left:460px">HOME</a>
    <a href="#" style="left:539px">ABOUT</a>
    <a href="#" style="left:624px">SERVICES</a>
    <a href="#" style="left:727px">TESTIMONIALS</a>
    <a href="#" style="left:860px">CONTACT US</a>
  </nav>
  <svg class="abs" style="left:1018px;top:46px" width="26" height="26" viewBox="0 0 26 26" fill="none" stroke="#fff" stroke-width="2.4"><circle cx="10" cy="10" r="7.5"/><path d="M15.5 15.5 23 23" stroke-linecap="round"/></svg>
</header>

<div class="hero-media abs" role="img" aria-label="Smiling doctor in a white coat seated at a desk in a bright clinic, soft hexagon backdrop"></div>
<h1 class="hero-title abs">WE BRING A</h1>
<p class="hero-line abs" style="top:374px">Solid medical industry experience,</p>
<p class="hero-line accent abs" style="top:406px">and a dedicated attitude to</p>
<p class="hero-line abs" style="top:438px">ensure quality customer service</p>
<a href="#" class="btn abs" style="left:144px;top:494px;width:151px;height:42px">Read More<svg viewBox="0 0 24 10" fill="none" stroke="currentColor" stroke-width="1.6"><path d="M0 5h22M17 1l5 4-5 4"/></svg></a>
<svg class="abs" style="left:0;top:600px" width="1200" height="220" viewBox="0 0 1200 220">
  <defs><linearGradient id="swooshA" x1="0" x2="1"><stop offset="0" stop-color="#3fb3a1"/><stop offset=".5" stop-color="#9bcb3c"/><stop offset="1" stop-color="#33a6d7"/></linearGradient></defs>
  <path d="M0 30 C200 120 420 200 640 198 C880 196 1060 140 1200 80 L1200 220 L0 220Z" fill="#fff"/>
  <path d="M0 20 C200 110 420 192 640 190 C880 188 1060 130 1200 70" fill="none" stroke="url(#swooshA)" stroke-width="14"/>
</svg>

<section>
  <div class="about-frame abs"></div>
  <svg class="abs" style="left:522px;top:989px" width="14" height="14"><circle cx="7" cy="7" r="5" fill="#9bcb3c"/></svg>
  <div class="abs" style="left:527px;top:895px;width:6px;height:96px;background:#fff"></div>
  <div class="about-photo abs" role="img" aria-label="Team of five medical professionals in scrubs and white coats"></div>
  <h2 class="section-title abs" style="left:584px;top:950px">ABOUT US</h2>
  <p class="about-text abs">Lorem ipsum dolor sit amet, consectetur adipiscing elit, sed do eiusmod tempor incididunt ut labore et dolore magna aliqua. Ut enim ad minim veniam, quis nostrud exercitation ullamco laboris nisi ut aliquip ex ea commodo consequat. Duis aute irure dolor in reprehenderit in voluptate velit esse cillum dolore eu fugiat nulla pariatur. Excepteur sint occaecat cupidatat non proident, sunt in culpa qui officia deserunt mollit anim id est laborum.Lorem ipsum dolor sit amet, consectetur adipiscing elit, sed do eiusmod tempor incididunt ut labore et dolore magna aliqua. Ut enim ad minim veniam, quis nostrud exercitation ullamco laboris nisi ut aliquip ex ea commodo consequat. Duis aute irure dolor in reprehenderit in voluptate velit esse cillum dolore eu fugiat nulla pariatur. Excepteur sint occaecat cupidatat non proident, sunt in culpa qui officia deserunt mollit anim id est laborum.</p>
  <a href="#" class="btn abs" style="left:874px;top:1297px;width:129px;height:36px;font-size:13px">Read More<svg viewBox="0 0 24 10" fill="none" stroke="currentColor" stroke-width="1.6"><path d="M0 5h22M17 1l5 4-5 4"/></svg></a>
</section>

<section>
  <h2 class="section-title abs" style="left:0;top:1470px;width:1200px;text-align:center;font-size:37px">BENEFITS OF OUTSOURCING MEDICAL BILLING INCLUDE:</h2>

  <div class="benefit-icon abs" style="left:47px;top:1563px"><svg width="58" height="50" viewBox="0 0 58 50" fill="none" stroke="#fff" stroke-width="3"><rect x="3" y="6" width="34" height="26" rx="3"/><rect x="9" y="14" width="34" height="26" rx="3" fill="#6fbf62"/><circle cx="38" cy="30" r="15" fill="#5db86b"/><path d="M43 24c-2-2-8-2-9 1s9 3 9 7-7 4-10 1M38 19v22"/></svg></div>
  <div class="benefit-icon abs" style="left:291px;top:1563px"><svg width="46" height="52" viewBox="0 0 46 52" fill="none" stroke="#fff" stroke-width="3"><path d="M23 3 41 10v14c0 13-8 21-18 25C13 45 5 37 5 24V10Z" fill="rgba(255,255,255,.25)"/><path d="M14 26l6 6 12-12"/></svg></div>
  <div class="benefit-icon abs" style="left:539px;top:1563px"><svg width="54" height="54" viewBox="0 0 54 54" fill="none" stroke="#fff" stroke-width="3"><circle cx="25" cy="29" r="21"/><circle cx="25" cy="29" r="13"/><circle cx="25" cy="29" r="5" fill="#fff"/><path d="M25 29 46 8M40 8h6v6"/></svg></div>
  <div class="benefit-icon abs" style="left:786px;top:1563px"><svg width="50" height="54" viewBox="0 0 50 54" fill="none" stroke="#fff" stroke-width="3"><path d="M3 20C6 8 16 3 25 3s19 5 22 17c-4-3-8-3-11 0-3-3-8-3-11 0-3-3-8-3-11 0-3-3-7-3-11 0Z" fill="#fff"/><path d="M25 20v6"/><path d="M31 32c-2-3-11-3-11 1s11 3 11 8-10 5-12 1M25 27v24"/></svg></div>
  <div class="benefit-icon abs" style="left:1033px;top:1563px"><svg width="52" height="48" viewBox="0 0 52 48" fill="none" stroke="#fff" stroke-width="3"><rect x="4" y="4" width="8" height="8"/><rect x="40" y="4" width="8" height="8"/><rect x="4" y="36" width="8" height="8"/><rect x="40" y="36" width="8" height="8"/><path d="M12 8h28M8 12v24M12 40c10-2 14-20 30-28"/></svg></div>

  <svg class="abs" style="left:170px;top:1600px" width="100" height="24" viewBox="0 0 100 24" fill="none" stroke="#222" stroke-width="1.5"><circle cx="4" cy="14" r="3"/><path d="M8 14c20 6 50 6 84-2" stroke-dasharray="4 3"/><path d="M88 8l6 4-6 4"/></svg>
  <svg class="abs" style="left:420px;top:1600px" width="100" height="24" viewBox="0 0 100 24" fill="none" stroke="#222" stroke-width="1.5"><circle cx="4" cy="12" r="3"/><path d="M8 12c20-6 55-8 84 2" stroke-dasharray="4 3"/><path d="M88 8l6 6-7 3"/></svg>
  <svg class="abs" style="left:668px;top:1600px" width="100" height="24" viewBox="0 0 100 24" fill="none" stroke="#222" stroke-width="1.5"><circle cx="4" cy="14" r="3"/><path d="M8 14c20 6 50 6 84-2" stroke-dasharray="4 3"/><path d="M88 8l6 4-6 4"/></svg>
  <svg class="abs" style="left:916px;top:1600px" width="100" height="24" viewBox="0 0 100 24" fill="none" stroke="#222" stroke-width="1.5"><circle cx="4" cy="12" r="3"/><path d="M8 12c20-6 55-8 84 2" stroke-dasharray="4 3"/><path d="M88 8l6 6-7 3"/></svg>

  <p class="benefit-label abs" style="left:-10px;top:1692px">Simplifying <b>financial</b><br>record-keeping</p>
  <p class="benefit-label abs" style="left:238px;top:1692px">Data <b>protection</b> for<br>sensitive files</p>
  <p class="benefit-label abs" style="left:485px;top:1692px">High <b>accuracy</b></p>
  <p class="benefit-label abs" style="left:736px;top:1692px">Quick turnaround time<br>for <b>insurance</b> claims</p>
  <p class="benefit-label abs" style="left:980px;top:1692px"><b>Scalability</b></p>
</section>

<section>
  <svg class="abs" style="left:0;top:1820px" width="1200" height="860" viewBox="0 0 1200 860">
    <defs>
      <linearGradient id="swooshB" x1="0" x2="1"><stop offset="0" stop-color="#3fb3a1"/><stop offset=".5" stop-color="#9bcb3c"/><stop offset="1" stop-color="#3fb3a1"/></linearGradient>
      <linearGradient id="swooshC" x1="0" x2="1"><stop offset="0" stop-color="#33a6d7"/><stop offset=".55" stop-color="#3fb3a1"/><stop offset="1" stop-color="#9bcb3c"/></linearGradient>
    </defs>
    <path d="M0 120 C200 40 420 12 620 14 C860 16 1060 60 1200 100 L1200 720 C1000 820 780 838 600 836 C380 834 180 790 0 720Z" fill="#f4f5f5"/>
    <path d="M0 100 C200 24 420 0 620 2 C860 4 1060 50 1200 90" fill="none" stroke="url(#swooshB)" stroke-width="16"/>
    <path d="M0 664 C180 740 380 824 600 826 C800 828 1000 790 1200 720" fill="none" stroke="url(#swooshC)" stroke-width="22"/>
  </svg>
  <h2 class="section-title abs" style="left:0;top:1960px;width:1200px;text-align:center">OUR&nbsp; MEDICAL BILLING SERVICES</h2>
  <div class="abs" style="left:571px;top:2013px;width:58px;height:3px;background:var(--green)"></div>

  <svg class="abs" style="left:142px;top:2200px" width="24" height="40" viewBox="0 0 24 40" fill="none" stroke="#222" stroke-width="2.5"><path d="M20 3 4 20l16 17"/></svg>
  <svg class="abs" style="left:1024px;top:2200px" width="24" height="40" viewBox="0 0 24 40" fill="none" stroke="#222" stroke-width="2.5"><path d="M4 3l16 17L4 37"/></svg>

  <div class="service-photo abs" style="left:193px;top:2098px;background:linear-gradient(135deg,#a87a4f,#e8e4dc 45%,#555 80%)" role="img" aria-label="Glasses, pen and calculator on a keyboard"></div>
  <div class="service-photo featured abs" style="left:474px;top:2098px;background:linear-gradient(135deg,#d7e4ea,#9fd2cf 50%,#6aa7b8)" role="img" aria-label="Nurse taking notes at a hospital workstation"></div>
  <div class="service-photo abs" style="left:754px;top:2098px;background:linear-gradient(135deg,#eef2f6,#c9d4de 50%,#555c66)" role="img" aria-label="Stethoscope resting on a billing statement"></div>

  <p class="service-name abs" style="left:183px;top:2354px">Medical Billing Service 1</p>
  <p class="service-name abs" style="left:464px;top:2354px">Medical Billing Service 2</p>
  <p class="service-name abs" style="left:744px;top:2354px">Medical Billing Service 3</p>
  <p class="service-desc abs" style="left:188px;top:2384px">Lorem ipsum dolor sit amet, consectetur adipiscing elit, sed do eiusmod tempor incididunt ut labore et dolore magna aliqua.</p>
  <p class="service-desc abs" style="left:469px;top:2384px">Lorem ipsum dolor sit amet, consectetur adipiscing elit, sed do eiusmod tempor incididunt ut labore et dolore magna aliqua.</p>
  <p class="service-desc abs" style="left:749px;top:2384px">Lorem ipsum dolor sit amet, consectetur adipiscing elit, sed do eiusmod tempor incididunt ut labore et dolore magna aliqua.</p>
  <a class="more abs" style="left:183px;top:2446px">Read More<svg viewBox="0 0 22 10" fill="none" stroke="currentColor" stroke-width="1.6"><path d="M0 5h20M15 1l5 4-5 4"/></svg></a>
  <a class="more abs" style="left:464px;top:2446px">Read More<svg viewBox="0 0 22 10" fill="none" stroke="currentColor" stroke-width="1.6"><path d="M0 5h20M15 1l5 4-5 4"/></svg></a>
  <a class="more abs" style="left:744px;top:2446px">Read More<svg viewBox="0 0 22 10" fill="none" stroke="currentColor" stroke-width="1.6"><path d="M0 5h20M15 1l5 4-5 4"/></svg></a>
  <a href="#" class="btn abs" style="left:513px;top:2503px;width:169px;height:36px;font-size:13px;background:#0b2430">View All Services<svg viewBox="0 0 24 10" fill="none" stroke="#fff" stroke-width="1.6"><path d="M0 5h22M17 1l5 4-5 4"/></svg></a>
</section>

<section>
  <div class="tasks-band abs" role="img" aria-label="Caregiver gently comforting a smiling elderly woman"></div>
  <h2 class="tasks-title abs">MEDICAL BILLING COMPANIES CAN<br>TAKE CARE OF CRUCIAL TASKS LIKE:</h2>
  <div class="task abs" style="top:2963px"><svg viewBox="0 0 32 32" fill="none" stroke="#fff" stroke-width="2.5"><circle cx="15" cy="17" r="12"/><path d="M9 16l6 6L30 4"/></svg>Patient Insurance Verification</div>
  <div class="task abs" style="top:3013px"><svg viewBox="0 0 32 32" fill="none" stroke="#fff" stroke-width="2.5"><circle cx="15" cy="17" r="12"/><path d="M9 16l6 6L30 4"/></svg>Medical Coding</div>
  <div class="task abs" style="top:3060px"><svg viewBox="0 0 32 32" fill="none" stroke="#fff" stroke-width="2.5"><circle cx="15" cy="17" r="12"/><path d="M9 16l6 6L30 4"/></svg>Claim Tracking</div>
  <div class="task abs" style="top:3107px"><svg viewBox="0 0 32 32" fill="none" stroke="#fff" stroke-width="2.5"><circle cx="15" cy="17" r="12"/><path d="M9 16l6 6L30 4"/></svg>Billing Analytics &amp; Reports</div>
</section>

<section>
  <h2 class="section-title abs" style="left:406px;top:3316px">WHAT OUR CLIENT SAY</h2>
  <div class="quote-photo abs"></div>
  <div class="quote-photo-inner abs" role="img" aria-label="Portrait of a smiling client with glasses"></div>
  <p class="quote-text abs">Lorem ipsum dolor sit amet, consectetur adipiscing elit, sed do eiusmod tempor incididunt ut labore et dolore magna aliqua. Ut enim ad minim veniam, quis nostrud exercitation ullamco laboris nisi ut aliquip ex ea commodo consequat. Duis aute irure dolor in reprehenderit in voluptate velit esse cillum dolore eu fugiat nulla pariatur. Lorem ipsum dolor sit amet, consectetur adipiscing elit, sed do eiusmod tempor incididunt ut labore et dolore magna aliqua.</p>
  <p class="client-name abs">Client's Name</p>
  <p class="client-role abs">Designation</p>
  <div class="dot abs" style="left:408px;top:3576px"></div>
  <div class="dot on abs" style="left:430px;top:3576px"></div>
  <div class="dot abs" style="left:452px;top:3576px"></div>
  <div class="dot abs" style="left:474px;top:3576px"></div>
  <div class="dot abs" style="left:496px;top:3576px"></div>
  <div class="pager abs" style="left:924px;top:3559px"><svg viewBox="0 0 24 10" fill="none" stroke="#888" stroke-width="1.6"><path d="M24 5H2M7 1 2 5l5 4"/></svg></div>
  <div class="pager abs" style="left:989px;top:3559px"><svg viewBox="0 0 24 10" fill="none" stroke="var(--green)" stroke-width="1.6"><path d="M0 5h22M17 1l5 4-5 4"/></svg></div>
</section>

<footer>
  <svg class="abs" style="left:0;top:3680px" width="1200" height="475" viewBox="0 0 1200 475">
    <defs><linearGradient id="swooshD" x1="0" x2="1"><stop offset="0" stop-color="#3fb3a1"/><stop offset=".5" stop-color="#9bcb3c"/><stop offset="1" stop-color="#87cfc6"/></linearGradient></defs>
    <path d="M0 130 C220 40 460 20 640 24 C880 30 1060 80 1200 150 L1200 475 L0 475Z" fill="#0d0d0d"/>
    <path d="M0 124 C220 34 460 14 640 18 C880 24 1060 74 1200 144" fill="none" stroke="url(#swooshD)" stroke-width="16"/>
  </svg>
  <div class="logo footer-logo abs">Tidewell Claimworks</div>
  <p class="footer-text abs">Lorem ipsum dolor sit amet, consectetur adipiscing elit, sed do eiusmod tempor incididunt ut labore et dolore magna aliqua. Ut enim ad minim veniam, quis nostrud exercitation ullamco laboris nisi ut aliquip ex ea commodo consequat.</p>
  <h3 class="footer-head abs" style="left:579px;top:3858px">Quick Links</h3>
  <ul class="quick-links abs">
    <li class="active">HOME</li>
    <li>ABOUT</li>
    <li>SERVICES</li>
    <li>TESTIMONIALS</li>
    <li>CONTACT US</li>
  </ul>
  <h3 class="footer-head abs" style="left:868px;top:3858px">Contact Us</h3>
  <div class="contact-row abs" style="top:3929px"><svg viewBox="0 0 28 22" fill="none" stroke="#fff" stroke-width="2"><path d="M5 3c-3 3-1 9 5 14s10 5 12 2l-4-4-3 2c-3-1-6-4-7-7l2-3Z"/><path d="M17 3a7 7 0 0 1 6 6M17 7a3 3 0 0 1 2 2"/></svg>(123) - 456 - 7890</div>
  <div class="abs" style="left:868px;top:3968px;width:174px;height:1px;background:#444"></div>
  <div class="contact-row abs" style="top:3982px"><svg viewBox="0 0 28 22" fill="none" stroke="#fff" stroke-width="2"><rect x="2" y="3" width="24" height="16"/><path d="M2 3l12 10L26 3M2 19l9-8M26 19l-9-8"/></svg>info@company.com</div>
  <p class="copyright abs">© 2020 Copyright- All Rights Reserved.</p>
</footer>

</body>
</html>
```